Banner Design

A law firm looking for a logo that can be used in a web banner that highlights the web address "splitpathcounsel.net" and incorporates our law firms name- Brantley and Associates. Would prefer a design with softer green color like Russian Green.

A preliminary thought would be a boxed banner with a Brantley and Associates logo on either side of the web address "splitpathcounsel.net".

Traditional and modern designs welcomed.
Updates

   Please make sure that "splitpathcounsel.net" is the main focus of the banner.  All advertising is being done to brand that website address.  Our law firm name/logo needs to be incorporated but not the focal point.  This banner will be listed at the top of every web page.

Designers feel free to go with an over/under design with splitpathcounsel.net going on top in a prominent position over our firm name. If that style sparks your creativity.  Remember this will be the banner design that will go on top of every page of the new website.        

                                I was thinking the firm name/logo on either side of the "splitpathcounsel.net" would look balanced. But from the designs that I have received maybe it would look more balance with the "splitpathcounsel.net" illustration over the firm name.

Target Market(s)

individuals 30-50

Industry/Entity Type

Law Firm

Logo Text

Brantley and Associates splitpathcounsel.net

Logo styles of interest
Emblem Logo
Wordmark Logo

```html
<!DOCTYPE html>
<html lang="en">
<head>
<meta charset="utf-8">
<title>splitpathcounsel.net banner</title>
<link rel="stylesheet" href="https://fonts.googleapis.com/css2?family=Arimo:wght@700&family=Noto+Serif:ital@1&display=swap">
<style>
  :root {
    --sage-deep: #233a29;
    --sage-dark: #3b5e43;
    --russian-green: #679267;
    --sage-light: #9cbf98;
    --white: #ffffff;
    --shadow: rgba(16, 32, 20, .85);
    --tab-sky: #3fa6d6;
    --tab-sky-dark: #2a7fb0;
    --tab-amber: #f2a01e;
    --tab-amber-dark: #d07c0c;
    --tab-navy: #3f62a8;
    --tab-navy-dark: #2b4784;
  }
  html, body { margin: 0; padding: 0; overflow: hidden; background: var(--sage-deep); }
  .banner {
    position: relative;
    width: 1200px;
    height: 174px;
    overflow: hidden;
    background: linear-gradient(90deg, var(--sage-deep) 0%, var(--sage-dark) 28%, var(--russian-green) 56%, var(--sage-dark) 82%, var(--sage-deep) 100%);
  }
  .banner__photo {
    position: absolute;
    left: 420px; top: 0;
    width: 780px; height: 174px;
    background:
      radial-gradient(ellipse 150px 120px at 280px 90px, rgba(190,225,185,.4), rgba(190,225,185,0) 70%),
      radial-gradient(ellipse 260px 160px at 560px 90px, rgba(20,40,25,.5), rgba(20,40,25,0) 75%);
  }
  .brand {
    position: absolute;
    left: 34px; top: 42px;
    margin: 0;
    font-family: "Arimo", Arial, sans-serif;
    font-weight: 700;
    font-size: 27px;
    line-height: 34px;
    color: var(--white);
  }
  .brand__line { display: block; white-space: nowrap; }
  .site-address {
    position: absolute;
    left: 276px; top: 62px;
    margin: 0;
    font-family: "Arimo", Arial, sans-serif;
    font-weight: 700;
    font-size: 52px;
    line-height: 1;
    color: var(--white);
    letter-spacing: .5px;
    white-space: nowrap;
    text-shadow: 2px 3px 4px var(--shadow);
  }
  .social {
    position: absolute; top: 0; left: 0;
    width: 1200px; height: 174px;
    pointer-events: none;
  }
  .social__label {
    font-family: "Noto Serif", Georgia, serif;
    font-style: italic;
    font-size: 12px;
    fill: var(--white);
  }
</style>
</head>
<body>
  <header class="banner">
    <div class="banner__photo" role="img" aria-label="Photograph of a magnifying glass over a dictionary page, in soft green light"></div>

    <p class="brand">
      <span class="brand__line">Brantley</span>
      <span class="brand__line">and Associates</span>
    </p>

    <h1 class="site-address">splitpathcounsel.net</h1>

    <svg class="social" viewBox="0 0 1200 174" aria-label="Social links">
      <defs>
        <linearGradient id="tab-sky" x1="0" y1="0" x2="0" y2="1">
          <stop offset="0" stop-color="var(--tab-sky)"/><stop offset="1" stop-color="var(--tab-sky-dark)"/>
        </linearGradient>
        <linearGradient id="tab-amber" x1="0" y1="0" x2="0" y2="1">
          <stop offset="0" stop-color="var(--tab-amber)"/><stop offset="1" stop-color="var(--tab-amber-dark)"/>
        </linearGradient>
        <linearGradient id="tab-navy" x1="0" y1="0" x2="0" y2="1">
          <stop offset="0" stop-color="var(--tab-navy)"/><stop offset="1" stop-color="var(--tab-navy-dark)"/>
        </linearGradient>
      </defs>
      <g class="social__tab">
        <path d="M886 0 H962 V88 L924 102 L886 88 Z" fill="url(#tab-sky)" stroke="var(--white)" stroke-width="3"/>
        <text class="social__label" x="924" y="68" text-anchor="middle">Chirper</text>
      </g>
      <g class="social__tab">
        <path d="M992 0 H1068 V88 L1030 102 L992 88 Z" fill="url(#tab-amber)" stroke="var(--white)" stroke-width="3"/>
        <text class="social__label" x="1030" y="68" text-anchor="middle">Feeds</text>
      </g>
      <g class="social__tab">
        <path d="M1098 0 H1174 V88 L1136 102 L1098 88 Z" fill="url(#tab-navy)" stroke="var(--white)" stroke-width="3"/>
        <text class="social__label" x="1136" y="68" text-anchor="middle">Friendbook</text>
      </g>
    </svg>
  </header>
</body>
</html>
```